Important Solar Energy Company Needs a Stationery Design

I need a modern, attractive, corporate stationary design (letter head and business card)
Attached Company Logo

Target Market(s)

Upmarket

Industry/Entity Type

Business

Colors
ec1f27
ffffff
757575
cbcbcb
000000

```html
<!DOCTYPE html>
<html lang="en">
<head>
<meta charset="utf-8">
<title>Solariva Stationery</title>
<link href="https://fonts.googleapis.com/css2?family=Questrial&display=swap" rel="stylesheet">
<style>
:root{
  --red:#ec1f27;
  --red-deep:#c41e25;
  --white:#ffffff;
  --grey:#757575;
  --grey-light:#cbcbcb;
  --ink:#000000;
  --stage:#e4e4e6;
  --paper:#fbfbfb;
}
*{margin:0;padding:0;box-sizing:border-box}
html,body{width:1200px;height:991px;overflow:hidden}
body{background:var(--stage);font-family:"Questrial",sans-serif;color:var(--ink);position:relative}
.sheet{position:absolute;overflow:hidden}
.wordmark{font-family:"Questrial",sans-serif;letter-spacing:.12em;white-space:nowrap}
.mark-dot{position:absolute;border-radius:50%}

/* Letterhead */
.letterhead{left:71px;top:104px;width:398px;height:561px;background:var(--paper)}
.letterhead .mark-dot{left:229px;top:33px;width:42px;height:42px;background:var(--red)}
.letterhead .wordmark{position:absolute;top:83px;left:0;width:100%;text-align:center;font-size:10px;color:var(--ink)}
.letter-body{position:absolute;left:33px;top:194px;width:334px;font-size:5.6px;line-height:7px;color:#222;text-align:justify}
.letter-body p{margin-bottom:5px}
.letter-body .salutation{font-weight:bold;margin-bottom:7px}
.sign-off{position:absolute;left:33px;top:365px;font-size:5.6px;line-height:7px}
.sign-off strong{display:block}
.signature{position:absolute;left:84px;top:355px;width:82px;height:42px;background:linear-gradient(135deg,#dfe2f2,#eef0f8);border-radius:3px}
.letter-footer{position:absolute;left:14px;right:14px;top:510px;display:flex}
.letter-footer .item{flex:1;text-align:center;font-size:5.2px;line-height:6.4px;color:#333;border-right:1px solid var(--grey-light);padding-top:1px;height:28px}
.letter-footer .item:last-child{border-right:none}
.letter-footer svg{display:block;margin:0 auto 4px;width:12px;height:12px}
.wave{position:absolute;left:0;bottom:0;width:100%}

/* Folder */
.folder{left:507px;top:90px;width:432px;height:575px;background:linear-gradient(120deg,#d1242b,#bd1d24 60%,#c2222a);border-radius:2px}
.folder .spine{position:absolute;left:27px;top:0;bottom:0;width:1px;background:rgba(0,0,0,.14)}
.folder .mark-dot{left:101px;top:78px;width:50px;height:50px;background:var(--white)}
.folder .wordmark{position:absolute;left:169px;top:90px;font-size:21px;color:var(--white)}
.folder .url{position:absolute;left:0;width:100%;top:531px;text-align:center;font-size:7px;color:var(--white)}

/* Business cards */
.card-front{left:68px;top:696px;width:169px;height:94px;background:var(--paper);border-radius:4px}
.card-front .mark-dot{left:36px;top:29px;width:28px;height:28px;background:var(--red)}
.card-front .wordmark{position:absolute;left:0;width:150px;padding-left:0;top:62px;font-size:7px;text-align:center;width:100px}
.card-front .divider{position:absolute;left:84px;top:14px;height:66px;width:1px;background:var(--grey-light)}
.card-details{position:absolute;left:96px;top:22px;font-size:4.2px;line-height:5.3px;color:#333}
.card-details .name{color:var(--red);font-weight:bold;font-size:5.2px;letter-spacing:.03em}
.card-details .role{margin-bottom:5px;color:var(--grey)}
.card-details .lbl{color:var(--red)}
.card-details .addr{margin-top:4px}
.card-back{left:68px;top:810px;width:169px;height:94px;background:var(--red-deep);border-radius:4px}
.card-back .mark-dot{left:30px;top:35px;width:24px;height:24px;background:var(--white)}
.card-back .wordmark{position:absolute;left:61px;top:41px;font-size:10px;color:var(--white)}

/* Envelopes */
.envelope-front{left:266px;top:696px;width:416px;height:209px;background:var(--paper)}
.envelope-front .mark-dot{left:36px;top:30px;width:40px;height:40px;background:var(--red)}
.envelope-front .wordmark{position:absolute;left:15px;top:75px;font-size:10px}
.envelope-front .return{position:absolute;left:24px;top:177px;font-size:5.4px;line-height:6.6px;color:#333}
.envelope-back{left:718px;top:696px;width:416px;height:209px;background:var(--paper)}
.envelope-back svg.flap{position:absolute;left:0;top:0}
.envelope-back .mark-dot{left:196px;top:19px;width:25px;height:25px;background:var(--white)}
.envelope-back .url{position:absolute;left:0;width:100%;top:183px;text-align:center;font-size:5.4px;color:#333}
.url b{color:var(--red);font-weight:normal}
</style>
</head>
<body>

<section class="sheet letterhead">
  <span class="mark-dot"></span>
  <div class="wordmark">SOLARIVA</div>
  <div class="letter-body">
    <p class="salutation">Dear sir,</p>
    <p>Energy choices shape the way a business grows. Our team designs solar systems that lower operating costs, protect budgets from rising tariffs and give every site a cleaner, quieter source of power. From the first survey to final commissioning, each project is planned around the needs of the people who use it.</p>
    <p>This year we completed installations for offices, warehouses and schools across the region, each one monitored around the clock by our engineers. Clients receive clear monthly reports showing output, savings and carbon avoided, so the value of their investment is always visible and easy to share with stakeholders.</p>
    <p>We would welcome the opportunity to review your current energy use and prepare a tailored proposal. A short site visit is all we need to outline the options, the expected payback period and the financing routes available to your organisation.</p>
    <p>Thank you for your time. We look forward to speaking with you soon and to helping your business run on clean, reliable power.</p>
  </div>
  <div class="sign-off">Yours Sincerely,<strong>Elena Marsh</strong></div>
  <div class="signature" role="img" aria-label="Handwritten signature of Elena Marsh"></div>
  <div class="letter-footer">
    <div class="item">
      <svg viewBox="0 0 12 12"><circle cx="6" cy="6" r="6" fill="#ec1f27"/><path d="M6 2.6a2.2 2.2 0 0 0-2.2 2.2C3.8 6.6 6 9.4 6 9.4s2.2-2.8 2.2-4.6A2.2 2.2 0 0 0 6 2.6z" fill="#fff"/><circle cx="6" cy="4.8" r=".8" fill="#ec1f27"/></svg>
      40 Harbor Lane, Suite 210<br>Brookfield, NY 11900
    </div>
    <div class="item">
      <svg viewBox="0 0 12 12"><circle cx="6" cy="6" r="6" fill="#ec1f27"/><path d="M4 3.2l1.1-.3.7 1.6-.7.5c.3.8.9 1.4 1.7 1.7l.5-.7 1.6.7-.3 1.1c-2.6.1-4.7-2-4.6-4.6z" fill="#fff"/></svg>
      (555) 014-2200
    </div>
    <div class="item">
      <svg viewBox="0 0 12 12"><circle cx="6" cy="6" r="6" fill="#ec1f27"/><rect x="3" y="4" width="6" height="4.2" fill="#fff"/><path d="M3 4l3 2.3L9 4" fill="none" stroke="#ec1f27" stroke-width=".6"/></svg>
      info@solariva.com
    </div>
    <div class="item">
      <svg viewBox="0 0 12 12"><circle cx="6" cy="6" r="6" fill="#ec1f27"/><g fill="none" stroke="#fff" stroke-width=".6"><circle cx="6" cy="6" r="3"/><ellipse cx="6" cy="6" rx="1.3" ry="3"/><path d="M3 6h6"/></g></svg>
      www.solariva.com
    </div>
  </div>
  <svg class="wave" viewBox="0 0 398 12" height="12" preserveAspectRatio="none"><path d="M50 12Q200 0 398 8V12Z" fill="#ec1f27"/></svg>
</section>

<section class="sheet folder">
  <span class="spine"></span>
  <span class="mark-dot"></span>
  <div class="wordmark">SOLARIVA</div>
  <div class="url">www.solariva.com</div>
</section>

<section class="sheet card-front">
  <span class="mark-dot"></span>
  <div class="wordmark">SOLARIVA</div>
  <span class="divider"></span>
  <div class="card-details">
    <div class="name">NORA WHITFIELD</div>
    <div class="role">General Manager</div>
    <div><span class="lbl">T:</span> (555) 014-2200</div>
    <div><span class="lbl">E:</span> info@solariva.com</div>
    <div><span class="lbl">W:</span> www.solariva.com</div>
    <div class="addr">40 Harbor Lane, Suite 210<br>Brookfield, NY 11900</div>
  </div>
  <svg class="wave" viewBox="0 0 169 6" height="6" preserveAspectRatio="none"><path d="M0 6Q80 0 169 5V6Z" fill="#ec1f27"/></svg>
</section>

<section class="sheet card-back">
  <span class="mark-dot"></span>
  <div class="wordmark">SOLARIVA</div>
</section>

<section class="sheet envelope-front">
  <span class="mark-dot"></span>
  <div class="wordmark">SOLARIVA</div>
  <div class="return">40 Harbor Lane, Suite 210<br>Brookfield, NY 11900</div>
  <svg class="wave" viewBox="0 0 416 8" height="8" preserveAspectRatio="none"><path d="M170 8Q300 1 416 2V8Z" fill="#ec1f27"/></svg>
</section>

<section class="sheet envelope-back">
  <svg class="flap" width="416" height="60" viewBox="0 0 416 60"><polygon points="0,0 416,0 398,58 16,58" fill="#d0222a"/></svg>
  <span class="mark-dot"></span>
  <div class="url">www.<b>solariva</b>.com</div>
</section>

</body>
</html>
```